Ferndale Chapel of Grace (this will be used for new church sign) sign will be 4'x8' and would like also listed Sunday School 9:00am Worship Service 10:30am.

Logo Text

FERNDALE CHAPEL OF GRACE

```html
<!DOCTYPE html>
<html lang="en">
<head>
<meta charset="utf-8">
<title>Ferndale Chapel of Grace – Church Sign</title>
<link rel="stylesheet" href="https://fonts.googleapis.com/css2?family=Fredoka:wght@600&family=Montserrat:wght@600;700&family=Ubuntu:wght@700&display=swap">
<style>
  :root {
    --backdrop: #231f20;
    --crimson: #c01f45;
    --gold: #c9a80c;
    --ink: #0d0d0d;
    --panel-light: #ffffff;
    --panel-shade: #dcdcdc;
    --mark-faint: rgba(150, 150, 150, 0.22);
  }
  * { margin: 0; padding: 0; box-sizing: border-box; }
  html, body {
    width: 1200px;
    height: 1200px;
    overflow: hidden;
    background: var(--backdrop);
  }
  .sign {
    position: absolute;
    left: 30px;
    top: 315px;
    width: 1140px;
    height: 570px;
    overflow: hidden;
    background: linear-gradient(100deg, var(--panel-shade) 0%, var(--panel-light) 42%, var(--panel-light) 55%, var(--panel-shade) 100%);
  }
  .sign__watermark {
    position: absolute;
    left: 766px;
    top: -28px;
    width: 384px;
    height: 384px;
    border-radius: 50%;
    background: var(--mark-faint);
  }
  .brand-dot {
    position: absolute;
    left: 90px;
    top: 72px;
    width: 180px;
    height: 180px;
    border-radius: 50%;
    background: var(--gold);
  }
  .church-name {
    position: absolute;
    left: 234px;
    top: 200px;
    color: var(--crimson);
    font-family: "Fredoka", sans-serif;
    font-weight: 600;
    line-height: 1;
  }
  .church-name__place {
    display: block;
    font-size: 30px;
    letter-spacing: 0.85em;
    margin-left: 60px;
  }
  .church-name__title {
    display: block;
    font-size: 64px;
    margin-top: 12px;
  }
  .rule {
    position: absolute;
    left: 234px;
    top: 332px;
    width: 780px;
    height: 2px;
    background: var(--gold);
  }
  .schedule {
    position: absolute;
    left: 254px;
    top: 356px;
    list-style: none;
    font-family: "Montserrat", sans-serif;
    font-weight: 600;
    font-size: 48px;
    line-height: 56px;
    color: var(--ink);
  }
  .schedule__sep,
  .schedule__time {
    color: var(--crimson);
    font-weight: 700;
  }
  .sign__stripe {
    position: absolute;
    left: 0;
    top: 480px;
    width: 100%;
    height: 8px;
    background: var(--crimson);
  }
  .contact-bar {
    position: absolute;
    left: 0;
    top: 488px;
    width: 100%;
    height: 82px;
    background: var(--ink);
    display: flex;
    align-items: center;
    padding-left: 58px;
    gap: 34px;
    font-family: "Ubuntu", sans-serif;
    font-weight: 700;
    font-size: 38px;
    color: var(--gold);
  }
  .contact-bar__item {
    display: flex;
    align-items: center;
    gap: 10px;
  }
  .contact-bar__icon {
    width: 28px;
    height: 28px;
    flex: none;
  }
</style>
</head>
<body>
  <main class="sign">
    <div class="sign__watermark" aria-hidden="true"></div>

    <div class="brand-dot" aria-hidden="true"></div>
    <h1 class="church-name">
      <span class="church-name__place">FERNDALE</span>
      <span class="church-name__title">Chapel of Grace</span>
    </h1>
    <div class="rule"></div>

    <ul class="schedule">
      <li>SUNDAY SCHOOL <span class="schedule__sep">|</span> <span class="schedule__time">9:00AM</span></li>
      <li>WORSHIP SERVICE <span class="schedule__sep">|</span> <span class="schedule__time">10:30AM</span></li>
    </ul>

    <div class="sign__stripe"></div>
    <footer class="contact-bar">
      <span class="contact-bar__item">
        <svg class="contact-bar__icon" viewBox="0 0 24 24" aria-hidden="true">
          <path fill="#c01f45" d="M6.6 10.8a15.1 15.1 0 0 0 6.6 6.6l2.2-2.2c.3-.3.7-.4 1-.2 1.1.4 2.3.6 3.6.6.6 0 1 .4 1 1V20c0 .6-.4 1-1 1A17 17 0 0 1 3 4c0-.6.4-1 1-1h3.5c.6 0 1 .4 1 1 0 1.3.2 2.5.6 3.6.1.3 0 .7-.2 1z"/>
        </svg>
        555.014.2390
      </span>
      <span class="contact-bar__item">
        <svg class="contact-bar__icon" viewBox="0 0 24 24" aria-hidden="true" fill="none" stroke="#c01f45" stroke-width="1.6">
          <circle cx="12" cy="12" r="10"/>
          <ellipse cx="12" cy="12" rx="4.5" ry="10"/>
          <line x1="2" y1="12" x2="22" y2="12"/>
          <line x1="4" y1="7" x2="20" y2="7"/>
          <line x1="4" y1="17" x2="20" y2="17"/>
        </svg>
        www.ferndalechapelofgrace.com
      </span>
    </footer>
  </main>
</body>
</html>
```